I need package design designs for an organic, natural, unrefined shea butter packaged in a pouch like the example below. The package design should express pure, organic, freshness, moisturizing and healthy. The package design should also reflect the benefits of the product listed below. The product will be called “ORGANIC SHEA BUTTER”
MEANING OF NAME: TOLU KENDRA" meaning to Come to Africa for your natural cosmetics
Logo Text/Brand Name:
“TOLU”
Logo Styles of Interest:
Elegance
Natural
Organic
Freshness
Unrefined
From a tree nut
Target Market:
General public
Must have:
KISS : Keep it simple stupid
Note: I have a shea nuts stock photo i can provide.
Dimension:W = 7.48 InchesH = 10.43 inches Added Thursday, January 14, 2016
Industry/Entity Type
Cosmetics

```html
<!DOCTYPE html>
<html lang="en">
<head>
<meta charset="utf-8">
<title>TOLU Shea Butter – Pouch Front</title>
<link rel="stylesheet" href="https://fonts.googleapis.com/css2?family=Montserrat:wght@900&family=Open+Sans:wght@400;600;700&display=swap">
<style>
  :root {
    --backdrop: #eceeef;
    --pouch: #f7f7f7;
    --pouch-edge: #e2e3e4;
    --brand-brown: #9a6c46;
    --label-tan: #b88a5f;
    --rule: #2a2a2a;
    --ink: #2b2b2b;
    --leaf: #6e9a4e;
    --leaf-dark: #3f6b2c;
    --nut: #8a5a36;
  }
  * { margin: 0; padding: 0; box-sizing: border-box; }
  html, body {
    width: 1200px;
    height: 1000px;
    overflow: hidden;
    background: var(--backdrop);
  }
  .canvas {
    position: relative;
    width: 1200px;
    height: 1000px;
  }
  .pouch-front {
    position: absolute;
    left: 330px;
    top: 30px;
    width: 540px;
    height: 940px;
    background: var(--pouch);
    border: 1px solid var(--pouch-edge);
    border-radius: 6px 6px 18px 18px;
    text-align: center;
  }
  .zip-seal {
    position: absolute;
    left: 0;
    right: 0;
    top: 110px;
    height: 40px;
    border-top: 1px solid var(--pouch-edge);
    border-bottom: 1px solid var(--pouch-edge);
  }
  .brand-name {
    position: absolute;
    left: 0;
    right: 0;
    top: 196px;
    font-family: "Montserrat", sans-serif;
    font-weight: 900;
    font-size: 140px;
    line-height: 1;
    letter-spacing: 2px;
    color: var(--brand-brown);
  }
  .brand-rule {
    position: absolute;
    left: 80px;
    right: 80px;
    top: 350px;
    height: 3px;
    background: var(--rule);
  }
  .product-name {
    position: absolute;
    left: 0;
    right: 0;
    top: 362px;
    font-family: "Open Sans", sans-serif;
    font-weight: 600;
    font-size: 42px;
    letter-spacing: 4px;
    line-height: 1.1;
    color: var(--label-tan);
  }
  .product-claims {
    position: absolute;
    left: 0;
    right: 0;
    top: 418px;
    font-family: "Open Sans", sans-serif;
    font-weight: 700;
    font-size: 18px;
    letter-spacing: 1px;
    color: var(--ink);
  }
  .product-claims .dot { margin: 0 6px; }
  .hero-photo {
    position: absolute;
    left: 90px;
    top: 462px;
    width: 360px;
    height: 362px;
  }
  .net-weight {
    position: absolute;
    left: 0;
    right: 0;
    top: 862px;
    font-family: "Open Sans", sans-serif;
    font-weight: 400;
    font-size: 22px;
    color: var(--ink);
  }
  .usage-note {
    position: absolute;
    left: 0;
    right: 0;
    top: 892px;
    font-family: "Open Sans", sans-serif;
    font-weight: 400;
    font-size: 24px;
    color: var(--ink);
  }
</style>
</head>
<body>
<main class="canvas">
  <section class="pouch-front">
    <div class="zip-seal"></div>
    <h1 class="brand-name">TOLU</h1>
    <div class="brand-rule"></div>
    <h2 class="product-name">SHEA BUTTER</h2>
    <p class="product-claims">Organic<span class="dot">•</span>Unrefined<span class="dot">•</span>Natural</p>
    <svg class="hero-photo" viewBox="0 0 360 362" role="img" aria-label="Photo of three shea nuts surrounded by green shea leaves">
      <defs>
        <radialGradient id="photoTone" cx="50%" cy="55%" r="50%">
          <stop offset="0%" stop-color="var(--nut)"/>
          <stop offset="38%" stop-color="var(--nut)" stop-opacity="0.85"/>
          <stop offset="55%" stop-color="var(--leaf)"/>
          <stop offset="85%" stop-color="var(--leaf-dark)" stop-opacity="0.5"/>
          <stop offset="100%" stop-color="var(--pouch)" stop-opacity="0"/>
        </radialGradient>
      </defs>
      <rect width="360" height="362" fill="url(#photoTone)"/>
    </svg>
    <p class="net-weight">16 OZ.</p>
    <p class="usage-note">External Use Only</p>
  </section>
</main>
</body>
</html>
```